Wedding Thank You post card

We would like to design a thank you post card for our wedding guests.
We want it to be a classic style with our photo and a simple 'Thank you' written and then Tom and Marcia 15.03.2014' Where the writing does not obstruct our image.
We need 140 post cards
Sorry for the delay please find some photos you can use for the design process. One or all photos can be used. Thank you

```html
<!DOCTYPE html>
<html lang="en">
<head>
<meta charset="utf-8">
<title>Wedding Thank You Post Card</title>
<link rel="stylesheet" href="https://fonts.googleapis.com/css2?family=Oranienbaum&family=Pinyon+Script&family=Cormorant+Garamond:ital,wght@1,600;1,700&display=swap">
<style>
  :root {
    --backdrop: #e8e5de;
    --card: #efebdc;
    --card-edge: #ddd7c2;
    --photo-sky: #dedccf;
    --photo-trees: #8e8a66;
    --photo-grass: #9c9657;
    --photo-road: #5d5d56;
    --photo-road-dark: #4f4f4a;
    --heading-grey: #8a8476;
    --rule: #a9a18a;
    --script-green: #86a23c;
    --accent-green: #b9d36a;
    --ink-brown: #5e4d22;
    --ink-dark: #3f3826;
  }
  * { box-sizing: border-box; margin: 0; padding: 0; }
  html, body { width: 1012px; height: 1200px; overflow: hidden; }
  body { background: var(--backdrop); position: relative; }

  .card { position: absolute; background: var(--card); border: 1px solid var(--card-edge); }

  /* Front */
  .card-front { left: 84px; top: 39px; width: 703px; height: 546px; padding: 14px; }
  .wedding-photo {
    width: 100%; height: 100%;
    background: linear-gradient(180deg,
      var(--photo-sky) 0%, var(--photo-sky) 8%,
      var(--photo-trees) 14%, var(--photo-grass) 22%, var(--photo-grass) 32%,
      var(--photo-road) 40%, var(--photo-road-dark) 100%);
    position: relative;
  }
  .date-tag {
    position: absolute; left: 531px; top: 373px; width: 109px; height: 119px;
    border: 2px solid var(--accent-green);
    display: flex; flex-direction: column; align-items: center; justify-content: center;
    color: var(--ink-brown); text-align: center;
  }
  .date-tag .tag-name { font-family: "Pinyon Script", cursive; font-size: 19px; line-height: 1; }
  .date-tag .tag-amp { font-family: "Pinyon Script", cursive; font-size: 14px; line-height: 1.1; }
  .date-tag .tag-date { font-family: "Cormorant Garamond", serif; font-style: italic; font-weight: 600; font-size: 11px; margin-top: 6px; }

  /* Back */
  .card-back { left: 214px; top: 606px; width: 707px; height: 548px; }
  .postcard-title {
    position: absolute; left: 353px; top: 28px; transform: translateX(-50%);
    font-family: "Oranienbaum", serif; font-size: 58px; line-height: 1;
    color: var(--heading-grey); white-space: nowrap;
  }
  .title-ornament {
    position: absolute; left: 270px; top: 98px; width: 166px; height: 22px;
    background: linear-gradient(90deg, transparent, rgba(138,132,118,.35), transparent);
  }
  .stamp-box { position: absolute; left: 589px; top: 35px; width: 88px; height: 102px; border: 1.5px solid var(--rule); }
  .divider { position: absolute; left: 352px; top: 118px; width: 2px; height: 384px; background: var(--rule); opacity: .8; }
  .address-lines { position: absolute; left: 383px; top: 0; width: 290px; height: 100%; }
  .address-lines span { position: absolute; left: 0; width: 100%; height: 2px; background: var(--rule); }

  .thank-you {
    position: absolute; left: 36px; top: 178px;
    font-family: "Pinyon Script", cursive; font-size: 72px; line-height: 1;
    color: var(--script-green); white-space: nowrap;
  }
  .green-rule { position: absolute; left: 46px; top: 289px; width: 264px; }
  .message {
    position: absolute; left: 181px; top: 318px; transform: translateX(-50%);
    font-family: "Cormorant Garamond", serif; font-style: italic; font-weight: 700;
    font-size: 17px; line-height: 24px; color: var(--ink-dark); text-align: center; white-space: nowrap;
  }
  .signature {
    position: absolute; left: 56px; top: 408px;
    font-family: "Pinyon Script", cursive; font-size: 36px; line-height: 1;
    color: var(--ink-brown); white-space: nowrap; font-weight: 700;
  }
  .signature .amp { font-size: 24px; }
</style>
</head>
<body>
  <section class="card card-front">
    <div class="wedding-photo" role="img" aria-label="Photograph of the bride and groom embracing on a driveway in front of a stone manor house and lawn">
      <div class="date-tag">
        <span class="tag-name">Tom</span>
        <span class="tag-amp">&amp;</span>
        <span class="tag-name">Marcia</span>
        <span class="tag-date">15.03.2014</span>
      </div>
    </div>
  </section>

  <section class="card card-back">
    <h1 class="postcard-title">Post Card</h1>
    <div class="title-ornament" role="img" aria-label="Small scroll ornament under the heading"></div>
    <div class="stamp-box"></div>
    <div class="divider"></div>
    <div class="address-lines">
      <span style="top:214px"></span>
      <span style="top:272px"></span>
      <span style="top:334px"></span>
      <span style="top:392px"></span>
    </div>

    <h2 class="thank-you">Thank You</h2>
    <svg class="green-rule" width="264" height="14" viewBox="0 0 264 14" aria-hidden="true">
      <line x1="0" y1="7" x2="264" y2="7" stroke="#b9d36a" stroke-width="2"/>
      <circle cx="132" cy="7" r="4" fill="#b9d36a"/>
    </svg>
    <p class="message">For Sharing In Our Joy<br>On Our Special Day</p>
    <p class="signature">Tom <span class="amp">&amp;</span> Marcia</p>
  </section>
</body>
</html>
```